Postcard Design

We need a postcard design for our 10 year anniversary open house. The company is Fernhollow Medical Spa. The web site is www.fernhollowmedicalspa-example.com. We want royal blue, sliver and white colors for the postcard along with a 10 Year image.

Industry/Entity Type

It Company

```html
<!DOCTYPE html>
<html lang="en">
<head>
<meta charset="utf-8">
<title>Fernhollow Medical Spa – 10th Anniversary Postcard</title>
<link rel="stylesheet" href="https://fonts.googleapis.com/css2?family=Cinzel:wght@600;700&family=Lato:ital,wght@0,400;0,700;1,700&display=swap">
<style>
  :root{
    --royal:#1b3fd6;
    --royal-deep:#0b1f8a;
    --royal-light:#3f63ee;
    --silver:#c9cbce;
    --silver-light:#f2f3f4;
    --silver-dark:#8e9196;
    --white:#ffffff;
    --ink:#222428;
    --page:#e6e7ea;
    --rule:#c4c6ca;
  }
  *{box-sizing:border-box;margin:0;padding:0}
  html,body{width:902px;height:1200px;overflow:hidden;background:var(--page)}
  body{position:relative;font-family:"Lato",sans-serif;color:var(--ink)}

  .postcard{position:absolute;left:66px;width:770px;height:500px;overflow:hidden;background:var(--white);box-shadow:0 6px 18px rgba(0,0,0,.25)}
  .postcard--front{top:40px}
  .postcard--back{top:640px}
  .postcard__art{position:absolute;inset:0;width:770px;height:500px}

  /* front */
  .brand{position:absolute;left:245px;top:14px;width:280px;text-align:center}
  .brand__name{display:inline-flex;align-items:center;gap:7px;font-family:"Lato",sans-serif;font-weight:700;font-size:17px;color:var(--royal)}
  .brand__dot{width:11px;height:11px;border-radius:50%;background:var(--royal)}
  .brand__tagline{display:block;margin-top:4px;font-size:9px;color:var(--royal-deep);letter-spacing:.3px}
  .headline{position:absolute;left:0;width:770px;text-align:center;font-family:"Cinzel",serif;font-weight:700;color:var(--silver-light);text-shadow:0 2px 3px rgba(0,0,0,.45)}
  .headline--lead{top:128px;font-size:40px;font-weight:600}
  .headline--main{top:190px;font-size:62px}
  .web-strip{position:absolute;left:0;top:452px;width:770px;text-align:center;font-size:17px;font-weight:700;letter-spacing:2px;color:var(--ink)}

  /* back */
  .tab{position:absolute;left:0;height:27px;padding:0 16px 0 12px;background:linear-gradient(var(--royal-light),var(--royal-deep));border-radius:0 14px 14px 0;color:var(--white);font-size:18px;font-weight:700;line-height:27px}
  .tab--about{top:20px}
  .tab--services{top:226px}
  .about-text{position:absolute;left:12px;top:58px;width:366px;font-size:12.2px;line-height:1.25;text-align:justify}
  .services{position:absolute;left:12px;top:260px;width:300px;display:grid;grid-template-columns:140px 150px;row-gap:8px;list-style:none}
  .service{display:flex;align-items:center;gap:8px;font-weight:700;font-style:italic;font-size:14px}
  .service--small{font-size:12.5px}
  .service__icon{width:28px;height:28px;border-radius:50%;background:var(--royal);border:2px solid var(--royal-deep);box-shadow:inset 0 0 0 3px var(--white)}
  .service__more{position:absolute;left:176px;top:98px;font-size:10px;font-weight:700;color:var(--royal)}
  .contact-bar{position:absolute;left:0;top:372px;width:390px;height:58px;background:linear-gradient(90deg,var(--royal-deep),var(--royal));color:var(--white);font-size:9.5px}
  .contact{position:absolute;display:flex;gap:7px;line-height:1.3}
  .contact svg{flex:none;margin-top:1px}
  .contact--phone{left:14px;top:8px}
  .contact--addr{left:14px;top:26px}
  .contact--mail{left:166px;top:8px}
  .contact--web{left:166px;top:26px}
</style>
</head>
<body>

<section class="postcard postcard--front" aria-label="Postcard front">
  <svg class="postcard__art" viewBox="0 0 770 500" aria-hidden="true">
    <defs>
      <linearGradient id="silverFrame" x1="0" x2="1">
        <stop offset="0" stop-color="#8e9196"/><stop offset=".5" stop-color="#f4f5f6"/><stop offset="1" stop-color="#8e9196"/>
      </linearGradient>
      <radialGradient id="royalPanel" cx=".5" cy=".35" r=".7">
        <stop offset="0" stop-color="#3f63ee"/><stop offset="1" stop-color="#0b1f8a"/>
      </radialGradient>
      <linearGradient id="glitter" x1="0" x2="1">
        <stop offset="0" stop-color="#9a9b9f"/><stop offset=".5" stop-color="#d8d9dc"/><stop offset="1" stop-color="#a3a4a8"/>
      </linearGradient>
    </defs>
    <rect width="770" height="500" fill="url(#silverFrame)"/>
    <path d="M0,100 Q385,15 770,112 L770,450 L0,450 Z" fill="#fff"/>
    <path d="M0,106 Q385,22 770,118 L770,450 L0,450 Z" fill="url(#royalPanel)"/>
    <path d="M245,0 L525,0 Q525,88 385,88 Q245,88 245,0 Z" fill="#fff"/>
    <rect x="0" y="310" width="770" height="136" fill="url(#glitter)" role="img" aria-label="Sparkling silver glitter band with a blue ribbon bow"/>
    <path d="M0,290 C150,330 260,340 385,318 C520,296 640,300 770,322 L770,345 C640,322 520,320 385,342 C260,362 150,352 0,315 Z" fill="#0b1f8a"/>
    <path d="M0,300 C150,336 260,344 385,326 C520,306 640,310 770,330" fill="none" stroke="#5b7cf2" stroke-width="2"/>
    <rect x="0" y="446" width="770" height="4" fill="#1b3fd6"/>
  </svg>
  <div class="brand">
    <span class="brand__name"><span class="brand__dot"></span>Fernhollow Medical Spa</span>
    <span class="brand__tagline">Cosmetic &amp; Laser Services</span>
  </div>
  <h1 class="headline headline--lead">Join Us for our</h1>
  <p class="headline headline--main">10th Anniversary</p>
  <p class="web-strip">www.fernhollowmedicalspa-example.com</p>
</section>

<section class="postcard postcard--back" aria-label="Postcard back">
  <svg class="postcard__art" viewBox="0 0 770 500" aria-hidden="true">
    <defs>
      <linearGradient id="swoosh" x1="0" x2="1">
        <stop offset="0" stop-color="#0b1f8a"/><stop offset="1" stop-color="#3f63ee"/>
      </linearGradient>
      <radialGradient id="photoWarm" cx=".5" cy=".45" r=".6">
        <stop offset="0" stop-color="#f1d6c2"/><stop offset="1" stop-color="#b9c8a0"/>
      </radialGradient>
      <radialGradient id="photoSoft" cx=".5" cy=".45" r=".6">
        <stop offset="0" stop-color="#f4e2d4"/><stop offset="1" stop-color="#c4b6a4"/>
      </radialGradient>
    </defs>
    <path d="M475,0 C410,90 400,260 430,420 L410,420 C370,260 385,90 455,0 Z" fill="url(#swoosh)"/>
    <path d="M500,0 C440,90 430,250 450,390 L440,390 C415,250 425,90 485,0 Z" fill="#c9cbce"/>
    <circle cx="452" cy="212" r="66" fill="#1b3fd6"/>
    <circle cx="452" cy="212" r="60" fill="url(#photoWarm)" role="img" aria-label="Photo of a client receiving a relaxing facial massage"/>
    <circle cx="440" cy="360" r="92" fill="#1b3fd6"/>
    <circle cx="440" cy="360" r="85" fill="url(#photoSoft)" role="img" aria-label="Photo of a client relaxing during a back massage"/>
    <rect x="645" y="38" width="95" height="102" fill="none" stroke="#9a9ca0" stroke-width="1.2"/>
    <g stroke="#c4c6ca" stroke-width="1.2">
      <line x1="540" y1="242" x2="740" y2="242"/>
      <line x1="540" y1="285" x2="740" y2="285"/>
      <line x1="540" y1="330" x2="740" y2="330"/>
    </g>
  </svg>

  <h2 class="tab tab--about">About Us</h2>
  <p class="about-text">Finally after centuries of searching for rejuvenation, there is something that really works. Laser (light amplification by stimulated emition of radiation) proved itself not only helpful in medical/surgical field. Over the last 10 years it has become clear that low dose of laser stimulates collagen, removes signs of aging, photocoagulates unwanted vascular lesions and removes unwanted hair by photoepilation. Laser treatments in combination with Lumivex injections, Dermaluxe and Collagen fillers offer enormous boost to looks and self esteem.</p>

  <h2 class="tab tab--services">Our Services</h2>
  <ul class="services">
    <li class="service"><span class="service__icon"></span>Massage</li>
    <li class="service service--small"><span class="service__icon"></span>Injectables</li>
    <li class="service"><span class="service__icon"></span>Lasers</li>
    <li class="service service--small"><span class="service__icon"></span>Facials</li>
    <li class="service"><span class="service__icon"></span>Healing Laser</li>
    <li class="service service--small"><span class="service__icon"></span>Chemical Peels</li>
    <li class="service__more">&amp; Other Services</li>
  </ul>

  <div class="contact-bar">
    <p class="contact contact--phone">
      <svg width="10" height="10" viewBox="0 0 10 10" aria-hidden="true"><path d="M2,0 L4,2.5 L3,4 Q4.5,6 6,7 L7.5,6 L10,8 L8.5,10 Q3,9 0,1.5 Z" fill="#fff"/></svg>
      555.014.2210
    </p>
    <p class="contact contact--addr">
      <svg width="10" height="10" viewBox="0 0 10 10" aria-hidden="true"><path d="M5,0 L10,5 L8.5,5 L8.5,10 L1.5,10 L1.5,5 L0,5 Z" fill="#fff"/></svg>
      <span>48 Alder Grove Rd., Ste 12<br>Maplewood, ST 00000</span>
    </p>
    <p class="contact contact--mail">
      <svg width="10" height="8" viewBox="0 0 10 8" aria-hidden="true"><rect width="10" height="8" fill="#fff"/><path d="M0,0 L5,4.5 L10,0" fill="none" stroke="#1b3fd6" stroke-width="1"/></svg>
      hello@fernhollowspa-example.com
    </p>
    <p class="contact contact--web">
      <svg width="10" height="10" viewBox="0 0 10 10" aria-hidden="true"><circle cx="5" cy="5" r="4.4" fill="none" stroke="#fff"/><ellipse cx="5" cy="5" rx="2" ry="4.4" fill="none" stroke="#fff"/><line x1=".6" y1="5" x2="9.4" y2="5" stroke="#fff"/></svg>
      www.fernhollowmedicalspa-example.com
    </p>
  </div>
</section>

</body>
</html>
```